依頼詳細
朝陽経済報を読むターゲットに対して
我々の広告を打ちます。

伝えたいことは「普通じゃダメなんです」
HPをご確認のうえ、ジムの印象などもご確認ください。
https://kx7fit.example/
記載項目
キャッチ:普通のおじさんでは、出世できない
リード:とはいえ、残念ながら日本は精神的に老化しやすい環境が揃っているそう。かっこよさは若い人の特権のように考えられ、『かっこよく歳を重ねる』という意識が少ない傾向にある。ぜひ、当ジムで「おじさん化対策」を実践して欲しい

黒地に白文字でのデザインを想定しております。
裏面に当社の情報をいれるため
引き付けて裏面をめくりたくなるようなA面のデザインを依頼させていただきます。
サイズ
A4
ページ数
片面
希望イメージ
シンプル 複雑
単色 カラフル
暗い 明るい
日常 高級
遊び心 厳粛
未来的 伝統的
女性的 男性的
希望する色
無彩色系
納品ファイル
• 高解像度JPG (.jpg)
• イラストレーター形式 (.ai)
補足説明
下記ロゴデータを画面どこかへ配置をお願いします。
我々で考えたデザイン案は下記になります。
これとは違うデザインをご提案いただきたいです。

「普通のおじさんでは出世できない」

提案いただいた中で、このキャッチを
「絶望」「恐怖」などで提案いただきましたが
「警告」として色味や主張をいただいた点が決め手となりました。
単色の差し色をも、新聞折り込みのチラシとしての相性も良く
弊社満場一致で可決となりました。

合計で60超の提案をいただきました。
皆様クリエイティブ溢れるアイディアをありがとうございました。

・キャッチコピーの受け取り方が想定と違う
・「おじさん」の中でもとらえられるイメージが違う

我々からの定義の中でも、
ご依頼方法を再考しないといけないなと考える学びもありました。
この度は皆様ご協力いただきありがとうございました!!

```html
<!DOCTYPE html>
<html lang="ja">
<head>
<meta charset="UTF-8">
<title>普通のおじさんでは出世できない｜KX7パーソナルジム</title>
<link href="https://fonts.googleapis.com/css2?family=Noto+Sans+JP:wght@400;500;700;900&family=Yuji+Boku&display=swap" rel="stylesheet">
<style>
  :root{
    --paper:#e4e4e4;
    --paper-light:#f2f2f2;
    --ink:#111111;
    --night:#0c0c0c;
    --night-soft:#2a2a2a;
    --white:#ffffff;
    --muted:#cfcfcf;
    --warning:#d8141b;
  }
  *{margin:0;padding:0;box-sizing:border-box;}
  html,body{width:849px;height:1200px;overflow:hidden;background:var(--night);}
  .flyer{
    position:relative;width:849px;height:1200px;overflow:hidden;
    font-family:"Noto Sans JP",sans-serif;
    background:linear-gradient(180deg,var(--paper-light) 0%,var(--paper) 30%,#9a9a9a 38%,var(--night-soft) 44%,var(--night) 60%,var(--night) 100%);
  }
  .photo-ordinary{
    position:absolute;left:0;top:0;width:470px;height:500px;
    background:linear-gradient(180deg,#cfcfcf 0%,#8d8d8d 45%,#3a3a3a 85%,rgba(20,20,20,0) 100%);
  }
  .photo-future{
    position:absolute;left:0;top:470px;width:470px;height:730px;
    background:linear-gradient(180deg,rgba(12,12,12,0) 0%,#2b2b2b 25%,#1a1a1a 60%,#0c0c0c 100%);
  }
  .headline-top{
    position:absolute;right:22px;top:14px;
    color:var(--ink);font-weight:900;font-size:112px;line-height:114px;
    letter-spacing:-2px;text-align:left;
  }
  .headline-bottom{
    position:absolute;right:14px;top:500px;
    color:var(--white);font-weight:900;font-size:112px;line-height:104px;
    letter-spacing:-2px;
  }
  .headline-bottom .indent{display:block;padding-left:112px;}
  .slogan{
    position:absolute;left:120px;top:462px;
    font-family:"Yuji Boku",serif;color:var(--warning);
    font-size:56px;letter-spacing:2px;transform:rotate(-2deg);
  }
  .lead{
    position:absolute;left:450px;top:702px;width:380px;color:var(--white);
  }
  .lead-open{font-size:30px;font-weight:700;margin-left:220px;margin-bottom:10px;}
  .lead-body{font-size:14.5px;line-height:1.85;font-weight:400;color:var(--muted);}
  .call{
    position:absolute;left:218px;top:985px;color:var(--white);
    font-size:16px;font-weight:500;line-height:1.6;
  }
  .call-key{font-size:30px;font-weight:900;display:block;margin:2px 0;letter-spacing:1px;}
  .brand{
    position:absolute;left:52px;top:1110px;display:flex;align-items:center;gap:12px;
    color:var(--white);
  }
  .brand-dot{width:34px;height:34px;border-radius:50%;background:var(--white);}
  .brand-name{font-size:24px;font-weight:700;line-height:1;}
  .brand-tag{font-size:10px;font-weight:400;color:var(--muted);margin-top:5px;letter-spacing:.5px;}
</style>
</head>
<body>
  <main class="flyer">
    <div class="photo-ordinary" role="img" aria-label="スーツ姿のくたびれた中年男性の写真（顔は画面外）"></div>
    <div class="photo-future" role="img" aria-label="暗がりに立つ引き締まったスーツ姿の男性の写真"></div>

    <h1 class="headline-top">普通の<br>おじさん<br>では</h1>
    <p class="slogan">未来は選べる</p>
    <p class="headline-bottom"><span class="indent">出世</span>できない</p>

    <section class="lead">
      <p class="lead-open">とはいえ、</p>
      <p class="lead-body">残念ながら日本は精神的に老化しやすい環境が揃っているそう。かっこよさは若い人の特権のように考えられ、『かっこよく歳を重ねる』という意識が少ない傾向にある。</p>
    </section>

    <p class="call">ぜひ、当ジムで<span class="call-key">「おじさん化対策」</span>を実践して欲しい</p>

    <div class="brand">
      <span class="brand-dot"></span>
      <div>
        <p class="brand-name">KX7パーソナルジム</p>
        <p class="brand-tag">The personal gym for grown men</p>
      </div>
    </div>
  </main>
</body>
</html>
```